Website Design for Gold Buying Company in Australia

We are looking for a Website layout for a company who buy gold pieces from trade and the public.

They would like to communicate that its easy, safe, a great way to make more money, and they pay the best prices in australia for Gold jewelery

Target Market(s)

Adults based in Australia aged 25-60 who are looking to make some extra money

Industry/Entity Type

It Company

Number of Pages Required

2 pages

Requirements
Must have
• Must have a homepage and a page to use for content.

• Will have a feed for the latest Gold, silver and platinum prices they are buying and selling at.

• Needs to have a from on the homepage where people can submit their details to be sent a ''Treasure Pouch'' which allows them to send gold pieces to eb valued and bought by the company.

Nice to have
• Would be nice to have a steped out graphic of how the ''Treasure Pouch by mail'' process works [Request a Kit, Send in your Gold, We Value and grade it, We pay you cash, cheque of Direct Deposit]

• Imagery will be gold related

• Colour schemes are not a major Issue-but using some gold or silver would be a good idea
Should not have
• No cheesy gold graphics please :)

```html
<!DOCTYPE html>
<html lang="en">
<head>
<meta charset="utf-8">
<title>Aurumline.com.au – Best prices in Australia</title>
<link href="https://fonts.googleapis.com/css2?family=Cinzel:wght@500;600&family=Lora:ital,wght@0,400;0,600;1,400&family=Open+Sans:wght@400;600;700&display=swap" rel="stylesheet">
<style>
:root{
  --gold:#c99a2e;
  --gold-light:#e2c067;
  --gold-text:#c8a03a;
  --cream:#f4ead2;
  --cream-dark:#e9dcb8;
  --brown:#4e4331;
  --brown-dark:#2f281d;
  --nav-text:#e7cf8c;
  --body-text:#6b6355;
  --line:#ddd0ab;
}
*{box-sizing:border-box;margin:0;padding:0}
html,body{width:1200px;height:741px;overflow:hidden;background:#fff}
body{font-family:"Open Sans",sans-serif;color:var(--body-text);position:relative}
.top-stripe{position:absolute;top:0;left:0;width:1200px;height:6px;background:var(--brown-dark)}
.header{position:absolute;top:6px;left:0;width:1200px;height:66px;background:linear-gradient(#f6eedb,#ece0c2);border-bottom:1px solid #cdb98a}
.brand{position:absolute;left:234px;top:14px;font-family:"Lora",serif;font-size:32px;color:var(--brown);letter-spacing:.5px}
.tagline{position:absolute;left:560px;top:26px;border-left:1px solid #c9b68c;padding-left:12px;font-family:"Lora",serif;font-style:italic;font-size:16px;color:#8a7d63}
.search{position:absolute;left:766px;top:22px;width:166px;height:22px;border:1px solid #d9cca9;background:#fbf7ec;font-size:10px;padding:4px 6px;color:#8a8272}
.search-icon{position:absolute;left:937px;top:23px}
.nav{position:absolute;top:72px;left:0;width:1200px;height:34px;background:linear-gradient(#6a5d46,#3b3325)}
.nav ul{position:absolute;left:226px;top:0;display:flex;list-style:none;height:34px}
.nav li{font-family:"Cinzel",serif;font-weight:500;font-size:11px;color:var(--nav-text);padding:0 6px;line-height:34px;border-right:1px solid #7b6d52}
.nav li.active{background:linear-gradient(#e8cd8a,#c9a558);color:var(--brown-dark);border:none}
.rates-title{position:absolute;left:232px;top:121px;width:478px;height:46px;background:linear-gradient(90deg,#f3efe6,#fbfaf6);font-family:"Lora",serif;font-size:27px;padding:6px 8px}
.rates-title b{color:var(--brown-dark);font-weight:600;font-style:italic}
.rates-title i{color:#9a8a66}
.rates{position:absolute;left:233px;top:170px;display:flex;gap:3px}
.rate{width:157px;height:108px;border:1px solid var(--line);background:var(--cream)}
.rate h3{height:30px;background:linear-gradient(#efe2bf,#e6d6ad);font-family:"Lora",serif;font-style:italic;font-weight:600;font-size:19px;color:#8c7e64;padding:0 8px;line-height:30px}
.rate-body{position:relative;height:76px}
.bar{position:absolute;left:6px;top:22px;width:64px;height:34px;border-radius:3px}
.bar.gold{background:linear-gradient(135deg,#fff09a,#e2b728)}
.bar.platinum{background:linear-gradient(135deg,#fafafa,#c9c9c9)}
.bar.silver{background:linear-gradient(135deg,#e2e2e2,#8f8f8f)}
.rate-body label{position:absolute;left:74px;font-size:8.5px;font-weight:600;color:#9a8f7a}
.rate-body .val{position:absolute;left:75px;width:75px;height:15px;border:1px solid #cfc2a2;background:#fdfaf1;font-size:8px;color:var(--gold-text);padding:1px 4px}
.article{position:absolute;left:232px;top:294px;width:478px}
.article h2{font-family:"Lora",serif;font-style:italic;font-weight:400;font-size:19px;color:var(--gold-text);margin-bottom:14px}
.article p{font-size:10px;line-height:15px;text-align:justify;margin-bottom:15px;letter-spacing:.1px}
.article p strong{color:#3c3528}
.btn-more{display:inline-block;background:var(--gold-light);border:1px solid #b58d2a;font-size:8.5px;font-weight:700;color:#4a3b17;padding:3px 5px;margin-top:-3px}
.rule{position:absolute;left:232px;top:499px;width:478px;height:2px;background:var(--line)}
.kit{position:absolute;left:724px;top:121px;width:232px}
.kit-ribbon{position:relative;height:64px;margin:0 -14px}
.kit-ribbon span{position:absolute;left:0;right:0;top:14px;text-align:center;font-family:"Lora",serif;font-weight:600;font-size:22px;color:var(--gold-light)}
.kit-panel{background:linear-gradient(#8b7d5e,#5e5239);height:232px;padding:10px 14px;color:#f5efe0}
.kit-panel h4{font-family:"Lora",serif;font-style:italic;font-weight:400;font-size:13px;color:var(--gold-light);margin-bottom:10px}
.kit-panel p{font-size:10px;line-height:15px;margin-bottom:12px}
.kit-panel label{display:block;font-size:9.5px;font-weight:600;color:#3a301f;margin-bottom:4px}
.kit-panel .field{height:20px;background:#fefcf5;border:1px solid #d5c9a8;font-size:8.5px;padding:3px 5px;color:#4a4234;margin-bottom:10px}
.send{float:right;margin-top:14px;background:var(--gold-light);border:1px solid #a8832c;font-family:"Lora",serif;font-style:italic;font-weight:600;font-size:11px;color:#4a3b17;padding:2px 7px}
.kit-foot{height:15px;background:var(--brown-dark)}
.footer-ornament{position:absolute;left:233px;top:528px;width:723px;height:84px;background:linear-gradient(180deg,rgba(226,197,128,0),rgba(213,178,98,.75))}
.footer-band{position:absolute;left:233px;top:610px;width:723px;height:63px;background:linear-gradient(#c59c37,#d8b14f 60%,#c09532);border-bottom:5px solid #6a5630}
.footer-band ul{display:flex;justify-content:center;list-style:none;margin-top:30px}
.footer-band li{font-family:"Cinzel",serif;font-weight:600;font-size:10px;color:#3a2e16;padding:0 8px;border-right:1px solid #a88430;line-height:20px}
.footer-band li:last-child{border:none}
.footer-site{position:absolute;left:233px;top:673px;width:723px;height:40px;background:linear-gradient(90deg,#dcd9d2,#fdfdfc 30%,#fdfdfc 70%,#dcd9d2);text-align:center;font-family:"Lora",serif;font-size:18px;color:var(--brown-dark);line-height:40px}
.copyright{position:absolute;left:0;top:719px;width:1178px;text-align:center;font-size:7.5px;color:#9a8b6c}
</style>
</head>
<body>
<div class="top-stripe"></div>
<header class="header">
  <div class="brand">Aurumline.com.au</div>
  <div class="tagline">Best prices in Australia</div>
  <div class="search">Search</div>
  <svg class="search-icon" width="18" height="18" viewBox="0 0 18 18"><circle cx="7" cy="7" r="5.5" fill="#f3f3f3" stroke="#9a9a9a" stroke-width="1.5"/><line x1="11" y1="11" x2="16.5" y2="16.5" stroke="#7a6a4a" stroke-width="3" stroke-linecap="round"/></svg>
</header>
<nav class="nav">
  <ul>
    <li>About Us</li><li>What We Buy &amp; Sell</li><li>How It Works</li><li>Commen Questions</li><li>Bullion</li><li>Contact Us</li><li class="active">Trade Enquires</li>
  </ul>
</nav>

<div class="rates-title"><b>Current</b> <i>Rates</i></div>
<section class="rates">
  <div class="rate"><h3>Gold</h3><div class="rate-body"><div class="bar gold" role="img" aria-label="Gold bar"></div><label style="top:3px">Buying</label><div class="val" style="top:15px">$32.3292/gg</div><label style="top:37px">Selling</label><div class="val" style="top:50px">$32.3292/gg</div></div></div>
  <div class="rate"><h3>Platinum</h3><div class="rate-body"><div class="bar platinum" role="img" aria-label="Platinum bar"></div><label style="top:3px">Buying</label><div class="val" style="top:15px">$32.3292/gg</div><label style="top:37px">Selling</label><div class="val" style="top:50px">$32.3292/gg</div></div></div>
  <div class="rate"><h3>Silver</h3><div class="rate-body"><div class="bar silver" role="img" aria-label="Silver bar"></div><label style="top:3px">Buying</label><div class="val" style="top:15px">$32.3292/gg</div><label style="top:37px">Selling</label><div class="val" style="top:50px">$32.3292/gg</div></div></div>
</section>

<article class="article">
  <h2>Lorem ipsum dolor</h2>
  <p>Nulla malesuada elementum lorem, ac bibendum dui molestie et. Morbi mattis imperdiet auctor. Maecenas iaculis tincidunt venenatis. Etiam cursus vulputate turpis, sed ornare ligula commodo sit amet. Donec nunc erat, feugiat auctor elementum a, condimentum vitae urna. Fusce malesuada nisi nec dolor vestibulum pellentesque.</p>
  <p>Phasellus nec nunc tincidunt velit congue dignissim consectetur eu odio. <strong>Sed nunc magna, congue eget pellentesque in, ullamcorper a nunc.</strong> In facilisis, mauris ac rhoncus posuere, mi nulla viverra nunc, non luctus erat orci non sem. Maecenas aliquet arcu a risus luctus id molestie.</p>
  <span class="btn-more">See more »</span>
</article>
<div class="rule"></div>

<aside class="kit">
  <div class="kit-ribbon">
    <svg width="260" height="64" viewBox="0 0 260 64"><path d="M0 58 L30 40 L40 10 Q130 -6 220 10 L230 40 L260 58 Q130 38 0 58Z" fill="#3e3426"/><path d="M40 10 Q130 -6 220 10 L230 44 Q130 30 30 44Z" fill="#5a4c36"/></svg>
    <span>Treasure Pouch</span>
  </div>
  <div class="kit-panel">
    <h4>Request a Kit, Send in your Gold</h4>
    <p>We Value and grade it, We pay you cash, cheque of Direct Deposit.</p>
    <label>Name</label>
    <div class="field">Mara Lindqvist</div>
    <label>E-mail</label>
    <div class="field">mara.lindqvist@mailbox.com</div>
    <span class="send">Send »</span>
  </div>
  <div class="kit-foot"></div>
</aside>

<div class="footer-ornament" role="img" aria-label="Decorative gold leaf and swirl pattern"></div>
<footer class="footer-band">
  <ul>
    <li>About Us</li><li>What We Buy &amp; Sell</li><li>How It Works</li><li>Commen Questions</li><li>Bullion</li><li>Contact Us</li><li>Trade Enquires</li>
  </ul>
</footer>
<div class="footer-site">www.aurumline.com.au</div>
<div class="copyright">Copyright © 2009 www.aurumline.com.au</div>
</body>
</html>
```